Bluefinch Painting needs a Website

We need a website built for a Painting company I own, we mainly do residential painting, but don't want to be limited to that.

Need to have estimate request form.
Need pic's of past projects

I like the look of the website for http://www.harborline-painters.example
& "Thistledown Property inspections"

My logo that was designed here on ArtHive on the front page

I would like one of the houses I downloaded as part of the background
of the front page.

Target Market(s)

Home owners

Industry/Entity Type

Painting

Number of Pages Required

1 page

Font styles to use
Serif

Requirements
Must have
• Estimate request form for home owners to fill out -
• Name:
• Phone Number:
• Address:
• E-mail:
• Painting project description:
• And my info to:
• My phone number: (555) 318-7764
• My web address bluefinchpainting.example
Nice to have
• My logo that was designed here on ArtHive

```html
<!DOCTYPE html>
<html lang="en">
<head>
<meta charset="utf-8">
<title>Bluefinch Painting</title>
<link rel="stylesheet" href="https://fonts.googleapis.com/css2?family=Marcellus&family=Crimson+Text:wght@400;600;700&family=Open+Sans:wght@400;600&display=swap">
<style>
:root{
  --blue:#2b7dbf;
  --blue-dark:#1d5f95;
  --ink:#1c1c1c;
  --muted:#8a8a8a;
  --dark:#16191d;
  --panel:#c7c7c7;
  --footer:#c9c9c9;
  --white:#ffffff;
  --photo-sky:#9fc3de;
  --photo-house:#8a7f6e;
  --photo-green:#5d7a45;
}
*{box-sizing:border-box;margin:0;padding:0}
html,body{width:1200px;height:3519px;overflow:hidden;background:var(--white)}
body{position:relative;font-family:"Crimson Text",Georgia,serif;color:var(--ink)}
.abs{position:absolute}

/* header */
.site-header{left:0;top:0;width:1200px;height:160px;background:var(--white)}
.social{right:160px;top:12px;display:flex;gap:8px}
.social span{width:30px;height:30px;background:#6d8fb8;border-radius:3px;display:block}
.search{right:30px;top:16px;width:110px;height:22px;border:1px solid #bbb;background:#fff}
.search i{position:absolute;right:-1px;top:-1px;width:22px;height:22px;background:#d5262e}
.brand{left:55px;top:96px;display:flex;align-items:center;gap:10px}
.brand-mark{width:34px;height:34px;background:var(--ink)}
.brand-name{font-family:"Crimson Text",serif;font-weight:600;font-size:30px;color:var(--ink);letter-spacing:.5px}
.nav{right:22px;top:96px;display:flex;gap:8px;font-family:"Open Sans",sans-serif;font-size:16px;font-weight:600}
.nav a{color:var(--blue);text-decoration:none;padding:8px 16px;border-radius:18px}
.nav a.active{background:var(--blue);color:var(--white)}

.hero{left:0;top:168px;width:1200px;height:484px;background:linear-gradient(180deg,var(--photo-sky) 0%,#b8cfe0 30%,var(--photo-house) 55%,var(--photo-green) 85%,#4a6236 100%)}

/* sections */
.section-title{width:1200px;left:0;text-align:center;font-family:"Marcellus",serif;color:var(--blue);font-size:50px;line-height:1}
.section-sub{width:1200px;left:0;text-align:center;font-weight:700;font-size:17px;line-height:1.35}
.about-text{left:105px;top:810px;width:990px;font-size:15.5px;line-height:1.45;color:var(--muted);text-align:justify}

.project{background:linear-gradient(170deg,var(--photo-sky),var(--photo-house) 55%,var(--photo-green))}

.services{left:106px;top:1894px;width:1003px;height:728px;background:radial-gradient(ellipse at 50% 40%,#2c343c,var(--dark) 75%)}
.services .section-title{color:var(--white);width:1003px}
.services .section-sub{color:var(--white);width:1003px}
.card{top:211px;width:248px}
.card-img{width:100%;height:226px;background:linear-gradient(170deg,#8fb7dc,#d9e4ee 50%,#6e8aa6)}
.card-title{margin-top:26px;font-weight:700;font-size:16px;color:var(--white);text-align:center}
.card-text{margin-top:8px;height:176px;overflow:hidden;font-size:13.5px;line-height:1.3;color:#8b939b;text-align:justify}
.btn-row{position:absolute;left:0;top:457px;width:100%;text-align:center}
.btn{display:inline-block;background:var(--blue);color:var(--white);font-family:"Open Sans",sans-serif;font-size:12px;font-weight:600;padding:6px 14px;border-radius:3px}

.testi-photo{width:132px;height:128px;background:linear-gradient(180deg,#3a3a3a,#121212)}
.testi-text{font-size:15px;line-height:1.25;color:var(--blue);text-align:justify;width:400px}
.testi-name{font-size:14px;font-style:italic;color:var(--ink);text-align:right;width:400px}

.form-box{left:739px;top:2721px;width:370px;height:412px;background:var(--panel)}
.form-row{display:flex;align-items:center;position:absolute;left:28px}
.form-row label{width:82px;font-weight:700;font-size:15px}
.form-row span{width:235px;height:30px;background:var(--white);display:block}
.form-area{left:28px;top:192px;width:317px;height:120px;background:var(--white);color:#aaa;font-size:14px;text-align:center;padding-top:6px}
.submit{left:137px;top:335px;background:var(--blue);color:var(--white);font-family:"Open Sans",sans-serif;font-size:14px;font-weight:600;padding:7px 24px;border-radius:16px}

.site-footer{left:0;top:3150px;width:1200px;height:369px;background:var(--footer)}
.foot-head{font-family:"Marcellus",serif;font-size:34px;color:var(--ink)}
.foot-links{font-size:20px;line-height:1.15;font-weight:600}
.contact{font-size:22px;line-height:1.3;font-weight:600}
.blog-photo{width:100px;height:110px;background:linear-gradient(180deg,#3a3a3a,#121212)}
.blog-text{font-size:14px;line-height:1.2;width:200px}
</style>
</head>
<body>

<header class="site-header abs">
  <div class="social abs" aria-label="Social links"><span></span><span></span><span></span><span></span></div>
  <div class="search abs"><i></i></div>
  <div class="brand abs"><span class="brand-mark"></span><span class="brand-name">Bluefinch Painting</span></div>
  <nav class="nav abs">
    <a class="active">Home</a><a>About Us</a><a>Services</a><a>Clients And Testimonials</a><a>FAQ</a><a>Contact Us</a>
  </nav>
</header>

<div class="hero abs" role="img" aria-label="Photo of a two-storey painted house with garden in front"></div>

<h2 class="section-title abs" style="top:686px">What we do?</h2>
<p class="section-sub abs" style="top:752px">Lorem ipsum dolor sit amet, consectetur adipisicing elit, sed do<br>eiusmod tempor incididunt utet dolore</p>
<p class="about-text abs">Lorem ipsum dolor sit amet, consectetur adipiscing elit. Aenean commodo ligula eget dolor. Aenean massa. Cum sociis natoque penatibus et magnis dis parturient montes, nascetur ridiculus mus. Donec quam felis, ultricies nec, pellentesque eu, pretium quis, sem. Nulla consequat massa quis enim. Donec pede justo, fringilla vel, aliquet nec, vulputate eget, arcu. In enim justo, rhoncus ut, imperdiet a, venenatis vitae, justo. Nullam dictum felis eu pede mollis pretium. Integer tincidunt. Cras dapibus. Vivamus elementum Lorem ipsum dolor sit amet, consectetur adipiscing elit. Aenean commodo ligula eget dolor. Aenean massa. Cum sociis natoque penatibus et magnis dis parturient montes, nascetur ridiculus mus. Donec quam felis, ultricies nec, pellentesque eu, pretium quis, sem. Nulla consequat massa quis enim. Donec pede justo, fringilla vel, aliquet nec, vulputate eget, arcu. In enim justo, rhoncus ut, imperdiet a, venenatis vitae, justo. Nullam dictum felis eu pede mollis pretium. Integer tincidunt. Cras dapibus.</p>

<h2 class="section-title abs" style="top:1000px">Our Projects</h2>
<p class="section-sub abs" style="top:1056px">Lorem ipsum dolor sit amet, consectetur adipisicing elit, sed do<br>eiusmod tempor incididunt utet dolore</p>

<div class="project abs" style="left:106px;top:1134px;width:324px;height:328px" role="img" aria-label="Project photo: grey two-storey house with flowering shrubs"></div>
<div class="project abs" style="left:440px;top:1134px;width:328px;height:320px" role="img" aria-label="Project photo: house with large tree and lawn"></div>
<div class="project abs" style="left:778px;top:1134px;width:331px;height:328px" role="img" aria-label="Project photo: house with wide driveway"></div>
<div class="project abs" style="left:106px;top:1472px;width:324px;height:394px" role="img" aria-label="Project photo: house with garage at dusk"></div>
<div class="project abs" style="left:440px;top:1464px;width:328px;height:402px" role="img" aria-label="Project photo: modern house with tall windows"></div>
<div class="project abs" style="left:778px;top:1472px;width:331px;height:394px" role="img" aria-label="Project photo: beige house with red flowers"></div>

<section class="services abs">
  <h2 class="section-title abs" style="top:70px">Our Services</h2>
  <p class="section-sub abs" style="top:120px">Lorem ipsum dolor sit amet, consectetur adipisicing elit, sed do<br>eiusmod tempor incididunt utet dolore</p>

  <div class="card abs" style="left:82px">
    <div class="card-img" role="img" aria-label="Photo of a freshly painted blue house"></div>
    <div class="card-title">Home Painting</div>
    <p class="card-text">Lorem ipsum dolor sit amet, consectetur adipiscing elit. Donec quam felis, ultricies nec, pellentesque eu, pretium quis, sem. Nulla consequat massa quis enim. Donec pede justo, fringilla vel, aliquet nec, vulputate eget, arcu. In enim justo, rhoncus ut, imperdiet a, venenatis vitae, justo. Nullam dictum felis eu pede mollis pretium. Integer tincidunt cras dapibus.</p>
    <div class="btn-row"><span class="btn">View Details</span></div>
  </div>

  <div class="card abs" style="left:377px">
    <div class="card-img" style="background:linear-gradient(170deg,#f3f3f3,#e2b6a6 55%,#c6483a)" role="img" aria-label="Photo of hands holding a small red house"></div>
    <div class="card-title">Interior Painting</div>
    <p class="card-text">Lorem ipsum dolor sit amet, consectetur adipiscing elit. Donec quam felis, ultricies nec, pellentesque eu, pretium quis, sem. Nulla consequat massa quis enim. Donec pede justo, fringilla vel, aliquet nec, vulputate eget, arcu. In enim justo, rhoncus ut, imperdiet a, venenatis vitae, justo. Nullam dictum felis eu pede mollis pretium. Integer tincidunt cras dapibus.</p>
    <div class="btn-row"><span class="btn">View Details</span></div>
  </div>

  <div class="card abs" style="left:670px">
    <div class="card-img" role="img" aria-label="Photo of a modern commercial building"></div>
    <div class="card-title">Commercial Painting</div>
    <p class="card-text">Lorem ipsum dolor sit amet, consectetur adipiscing elit. Donec quam felis, ultricies nec, pellentesque eu, pretium quis, sem. Nulla consequat massa quis enim. Donec pede justo, fringilla vel, aliquet nec, vulputate eget, arcu. In enim justo, rhoncus ut, imperdiet a, venenatis vitae, justo. Nullam dictum felis eu pede mollis pretium. Integer tincidunt cras dapibus.</p>
    <div class="btn-row"><span class="btn">View Details</span></div>
  </div>
</section>

<h2 class="abs foot-head" style="left:114px;top:2660px;color:var(--blue);font-size:44px">Testimonials</h2>
<h2 class="abs foot-head" style="left:790px;top:2660px;color:var(--blue);font-size:44px">Request Form</h2>

<div class="testi-photo abs" style="left:125px;top:2730px" role="img" aria-label="Client portrait"></div>
<p class="testi-text abs" style="left:284px;top:2728px">There are many variations of passages of Lorem Ipsum available, but the majority have suffered alteration in some form, by injected humour, or randomised words which don't look even slightly believable. If you are going to use.</p>
<div class="testi-name abs" style="left:284px;top:2830px">-John Doe</div>

<div class="testi-photo abs" style="left:125px;top:2868px" role="img" aria-label="Client portrait"></div>
<p class="testi-text abs" style="left:284px;top:2872px">There are many variations of passages of Lorem Ipsum available, but the majority have suffered alteration in some form, by injected humour, or randomised words which don't look even slightly believable. If you are going to use.</p>
<div class="testi-name abs" style="left:284px;top:2970px">-John Doe</div>

<div class="testi-photo abs" style="left:125px;top:3004px" role="img" aria-label="Client portrait"></div>
<p class="testi-text abs" style="left:284px;top:3006px">There are many variations of passages of Lorem Ipsum available, but the majority have suffered alteration in some form, by injected humour, or randomised words which don't look even slightly believable. If you are going to use.</p>
<div class="testi-name abs" style="left:284px;top:3104px">-John Doe</div>

<form class="form-box abs">
  <div class="form-row" style="top:30px"><label>Name</label><span></span></div>
  <div class="form-row" style="top:70px"><label>Phone No.</label><span></span></div>
  <div class="form-row" style="top:110px"><label>Address</label><span></span></div>
  <div class="form-row" style="top:150px"><label>Email</label><span></span></div>
  <div class="form-area abs">Write Your comments here</div>
  <div class="submit abs">Submit</div>
</form>

<footer class="site-footer abs">
  <h3 class="foot-head abs" style="left:108px;top:62px">Quick Links</h3>
  <div class="foot-links abs" style="left:114px;top:112px">Home<br>About Us<br>Services<br>Client &amp;Testimonials<br>FAQ<br>Contact Us</div>

  <h3 class="foot-head abs" style="left:452px;top:62px">Latest Blog &amp; News</h3>
  <div class="blog-photo abs" style="left:456px;top:115px" role="img" aria-label="Blog post photo"></div>
  <p class="blog-text abs" style="left:566px;top:112px">Here are many variations of passages of Lorem Ipsum available, but the majority have suffered alteration in some form by humour.</p>
  <div class="abs" style="left:640px;top:242px;font-size:11px">Posted On July 2015</div>

  <h3 class="foot-head abs" style="left:834px;top:62px">Contact Info</h3>
  <div class="contact abs" style="left:840px;top:120px">Bluefinch Painting<br>Phone No.: (555) 318-7764<br>bluefinchpainting.example</div>
</footer>

</body>
</html>
```